Student project platform needs an awareness flyer

Tornuvel is a matchmaking and crowdfunding site for student projects. On this platform, students can team up with each other to invent a new product, innovate, or start a business. They can also raise funds for their project.

** I am in need of an 8x11" flyer to print and distribute digitally which notifies students of all different skill sets that this site exists.

The flyer should communicate that a diverse user base is being built on this site, with people who have skills in programming, engineering, design, business, finance, and so on.

The flyer should also be clean and modern, with an emphasis on creativity and innovation. I've attached the business' logo to give you an idea of the artistic style we have already established.

Target Market(s)

University students

Industry/Entity Type

Crowdfunding

Font styles to use
Serif
Sans Serif

Requirements
Must have
• * Clean and modern design
• * Color scheme of my logo: #336699 and #669933 (blue and green)
• * Convey that this site is for people of different skill sets: programming, engineering, design, business, finance, and so on.
• * See the attached "Tornuvel Copy.txt" for text to include on the flyer

```html
<!DOCTYPE html>
<html lang="en">
<head>
<meta charset="utf-8">
<title>Tornuvel Student Flyer</title>
<link rel="stylesheet" href="https://fonts.googleapis.com/css2?family=Lato:wght@300;400;700;900&display=swap">
<style>
  :root {
    --brand-blue: #336699;
    --brand-green: #669933;
    --panel-green: #5f9a22;
    --ink: #2b2b2b;
    --body-ink: #3a3a3a;
    --band-dark: #3d3d3d;
    --band-darker: #2a2a2a;
    --paper: #ffffff;
    --backdrop: #e6e6e6;
  }
  * { margin: 0; padding: 0; box-sizing: border-box; }
  html, body { width: 1200px; height: 1200px; overflow: hidden; }
  body {
    background: var(--backdrop);
    font-family: "Lato", sans-serif;
    color: var(--ink);
  }
  .flyer {
    position: absolute;
    left: 184px; top: 30px;
    width: 832px; height: 1140px;
    background: var(--paper);
    box-shadow: 0 6px 24px rgba(0,0,0,.25);
    overflow: hidden;
  }
  .flyer-art { position: absolute; inset: 0; }
  .block { position: absolute; }
  .brand-name {
    left: 60px; top: 595px; width: 200px; text-align: center;
    font-size: 36px; font-weight: 400; color: var(--brand-blue); letter-spacing: 1px;
  }
  .lead-in { left: 33px; top: 651px; font-size: 20px; font-weight: 400; color: var(--body-ink); }
  .headline {
    left: 33px; top: 674px; font-size: 36px; font-weight: 900; line-height: 34px; color: var(--ink);
  }
  .headline em { font-style: normal; color: var(--brand-green); }
  .join { left: 33px; top: 760px; font-size: 38px; font-weight: 400; color: var(--ink); }
  .join strong { font-weight: 900; color: var(--brand-blue); }
  .join-sub { left: 33px; top: 806px; font-size: 18px; font-weight: 400; color: var(--body-ink); }
  .join-skills { left: 33px; top: 828px; font-size: 24px; font-weight: 700; color: var(--brand-blue); }
  .join-skills span { color: var(--ink); }
  .about-title { left: 33px; top: 877px; font-size: 20px; font-weight: 700; color: var(--brand-blue); }
  .about-text {
    left: 33px; top: 902px; width: 362px;
    font-size: 19px; line-height: 24.5px; text-align: justify; color: var(--body-ink);
  }
  .site-url {
    left: 0; top: 1089px; width: 446px; text-align: center;
    font-size: 22px; letter-spacing: 4px; color: #fff;
  }
  .call-out {
    left: 520px; top: 619px; font-size: 26px; line-height: 32px; font-weight: 400; color: #fff;
  }
  .goal { left: 520px; font-size: 37px; font-weight: 400; color: #fff; }
  .goal-build { top: 698px; }
  .goal-invent { top: 807px; }
  .goal-innovate { top: 921px; }
  .goal-business { top: 1034px; }
</style>
</head>
<body>
<main class="flyer">
  <svg class="flyer-art" width="832" height="1140" viewBox="0 0 832 1140">
    <defs>
      <linearGradient id="photo-tone" x1="0" y1="0" x2="0" y2="1">
        <stop offset="0" stop-color="#cfd2cc"/>
        <stop offset=".55" stop-color="#8f8f86"/>
        <stop offset="1" stop-color="#6c6350"/>
      </linearGradient>
      <linearGradient id="band-tone" x1="0" y1="0" x2="1" y2="0">
        <stop offset="0" stop-color="var(--band-dark)"/>
        <stop offset="1" stop-color="var(--band-darker)"/>
      </linearGradient>
      <linearGradient id="panel-tone" x1="0" y1="0" x2="1" y2="0">
        <stop offset="0" stop-color="#5a9320"/>
        <stop offset="1" stop-color="#65a528"/>
      </linearGradient>
    </defs>

    <!-- header photo area -->
    <polygon points="0,0 832,0 832,392 396,594 0,387" fill="url(#photo-tone)"
             role="img" aria-label="Photo of a diverse group of smiling university students leaning against a wall"/>
    <polyline points="0,390 396,598 832,396" fill="none" stroke="var(--brand-blue)" stroke-width="5"/>

    <!-- bottom band -->
    <polygon points="0,1080 832,968 832,1140 0,1140" fill="var(--brand-green)"/>
    <polygon points="0,1090 832,978 832,1140 0,1140" fill="url(#band-tone)"/>

    <!-- green call-out panel -->
    <polygon points="446,639 808,481 808,1116 446,1116" fill="url(#panel-tone)"/>

    <!-- brand mark -->
    <circle cx="160" cy="552" r="44" fill="var(--brand-blue)"/>

    <!-- icon: build (bricks) -->
    <g transform="translate(457,720)">
      <circle r="41" fill="#fff"/>
      <circle r="33" fill="var(--brand-blue)"/>
      <g fill="none" stroke="#fff" stroke-width="2">
        <path d="M-18,-12 h8 v6 h-8z M-10,-6 h8 v6 h-8z M-18,0 h8 v6 h-8z M-2,0 h8 v6 h-8z M-10,6 h8 v6 h-8z M6,6 h8 v6 h-8z M-18,12 h36"/>
        <path d="M-2,-18 h8 v6 h-8z M6,-6 h8 v6 h-8z M14,0 h6 v6 h-6z"/>
      </g>
    </g>
    <!-- icon: invent (bulb over hand) -->
    <g transform="translate(457,832)">
      <circle r="41" fill="#fff"/>
      <circle r="33" fill="var(--brand-blue)"/>
      <g fill="none" stroke="#fff" stroke-width="2" stroke-linecap="round">
        <circle cx="0" cy="-9" r="9"/>
        <path d="M-4,0 v5 h8 v-5 M-3,8 h6"/>
        <path d="M-20,14 q8,-6 16,0 h10 q6,-4 12,-6 M-20,20 h24 l16,-10"/>
      </g>
    </g>
    <!-- icon: innovate (gear) -->
    <g transform="translate(457,945)">
      <circle r="41" fill="#fff"/>
      <circle r="33" fill="var(--brand-blue)"/>
      <g fill="none" stroke="#fff" stroke-width="2.5">
        <circle r="10"/>
        <circle r="4"/>
        <path d="M0,-16 v5 M0,11 v5 M-16,0 h5 M11,0 h5 M-11,-11 l4,4 M7,7 l4,4 M11,-11 l-4,4 M-7,7 l-4,4"/>
      </g>
    </g>
    <!-- icon: start a business (flag) -->
    <g transform="translate(457,1057)">
      <circle r="41" fill="#fff"/>
      <circle r="33" fill="var(--brand-blue)"/>
      <g fill="#fff">
        <rect x="-3" y="-18" width="3" height="30"/>
        <path d="M0,-18 h16 l-5,6 l5,6 h-16z"/>
        <rect x="-12" y="12" width="21" height="5" rx="1"/>
      </g>
    </g>
  </svg>

  <div class="block brand-name">TORNUVEL</div>

  <p class="block lead-in">Find a team of students and crowdfund</p>
  <h1 class="block headline">your next <em>invention</em><br>or <em>company</em></h1>

  <p class="block join">Join <strong>Tornuvel</strong></p>
  <p class="block join-sub">to support and lend</p>
  <p class="block join-skills">your skills to student projects<span>!</span></p>

  <h2 class="block about-title">What is Tornuvel?</h2>
  <p class="block about-text">Tornuvel is a matchmaking and crowd-funding platform for student projects. It allows students to form teams of diverse skills and raise money to build, innovate, invent, or start a business.</p>

  <p class="block site-url">www.tornuvel.com</p>

  <p class="block call-out">Calling all students<br>who want to</p>
  <p class="block goal goal-build">Build</p>
  <p class="block goal goal-invent">Invent</p>
  <p class="block goal goal-innovate">Innovate</p>
  <p class="block goal goal-business">Start a business</p>
</main>
</body>
</html>
```